Re-Design of a 1 Pager IT Security Website

Please create a 1 Pager design for this website and all its elements: http://www.pelmarokvistaqueen.com/

Colours, Fonts etc: You can select whatever you prefer

```html
<!DOCTYPE html>
<html lang="en">
<head>
<meta charset="utf-8">
<title>Domain Monitoring</title>
<link href="https://fonts.googleapis.com/css2?family=Lato:wght@400;700;900&family=Merriweather:wght@400&display=swap" rel="stylesheet">
<style>
:root{
  --navy:#1c2463;
  --navy-deep:#151b4e;
  --blue:#2f8fe2;
  --blue-light:#52a8f0;
  --card:#e6f2fc;
  --ink:#1c2463;
  --text:#333a4a;
  --white:#ffffff;
  --line:#d4d8e2;
}
*{box-sizing:border-box;margin:0;padding:0}
html,body{width:1200px;height:5263px;overflow:hidden;background:var(--white)}
body{position:relative;font-family:'Merriweather',serif;color:var(--text)}
.abs{position:absolute}
h1,h2,h3,h4,.nav,.btn,.label{font-family:'Lato',sans-serif}
.heading{font-family:'Lato',sans-serif;font-weight:900;color:var(--ink);font-size:42px;line-height:62px;text-transform:uppercase}
.heading.light{color:var(--white)}
.copy{font-size:14.5px;line-height:30px;color:var(--text)}
.copy.light{color:var(--white)}
.btn{position:absolute;height:46px;padding:0 24px;border-radius:23px;background:var(--blue);color:var(--white);font-size:14px;font-weight:700;line-height:46px;text-transform:uppercase;letter-spacing:.3px}
.btn.outline{background:transparent;border:2px solid var(--white);line-height:42px}
.btn.outline-blue{background:var(--blue);border:2px solid var(--white);line-height:42px}
.topbar{left:0;top:0;width:1200px;height:78px;background:var(--navy)}
.brand{left:98px;top:20px;font-family:'Lato',sans-serif;font-weight:700;font-size:31px;color:var(--white);letter-spacing:.3px}
.nav{right:98px;top:22px;display:flex;gap:8px}
.nav a{color:var(--white);font-size:15px;text-decoration:none;padding:6px 14px;border-radius:4px}
.nav a.active{background:#3a4284}
.hero-title{left:98px;top:195px;font-size:50px;line-height:64px;color:var(--white)}
.hero-art{left:560px;top:110px;width:560px;height:420px;border-radius:30px;background:radial-gradient(ellipse at center,#3f62c8 0%,#2b3d98 45%,rgba(28,36,99,0) 75%)}
.video{left:98px;top:883px;width:458px;height:364px;border:2px solid #2a2a6a;border-radius:40px;background:linear-gradient(135deg,#f4f5fb,#ffffff 55%,#eadcf8);overflow:hidden}
.play{left:201px;top:165px;width:34px;height:24px;border-radius:6px;background:#222}
.play::after{content:"";position:absolute;left:13px;top:7px;border-left:10px solid #fff;border-top:5px solid transparent;border-bottom:5px solid transparent}
.risk-card{position:absolute;width:233px;background:var(--card);box-shadow:0 6px 18px rgba(30,40,90,.15);text-align:center;padding:28px 18px 0}
.risk-card h4{font-weight:700;font-size:18px;color:var(--ink);margin:14px 0 8px}
.risk-card p{font-size:10.5px;line-height:16px;color:var(--text)}
.risk-card .more{display:block;margin-top:22px;font-family:'Lato',sans-serif;font-size:10px;font-weight:700;color:var(--ink);text-decoration:underline}
.photo-keys{left:82px;top:2207px;width:343px;height:471px;background:linear-gradient(160deg,#0f2447,#1e5a9a 50%,#b98b79)}
.data-box{left:307px;top:2355px;width:245px;height:245px;background:linear-gradient(160deg,#2e8be0,#1d4da3);text-align:center;color:var(--white);padding-top:130px;font-size:18px;line-height:31px}
.mon-card{position:absolute;width:222px;height:235px;background:var(--card);text-align:center;border-radius:6px;padding-top:30px}
.mon-card h4{font-size:14px;font-weight:700;color:var(--ink);margin-top:20px}
.mon-card p{font-size:13px;line-height:22px;margin-top:10px;color:var(--text)}
.photo-desk{left:691px;top:3812px;width:413px;height:388px;border-radius:70px 0 70px 0;border:4px solid var(--navy);background:linear-gradient(150deg,#6a7a8c,#2f3a4a 60%,#98a5b5)}
.field{position:absolute;height:45px;border:1px solid #c9ccd6;font-family:'Lato',sans-serif;font-size:14px;color:#333;padding:12px 18px}
.foot-h{font-family:'Lato',sans-serif;font-weight:700;font-size:27px;color:var(--white);text-transform:uppercase}
.foot-t{font-size:14px;line-height:26px;color:var(--white)}
.foot-links{left:0;top:5160px;width:1200px;display:flex;justify-content:center;gap:44px}
.foot-links a{color:var(--white);font-family:'Lato',sans-serif;font-size:15px;text-decoration:none}
.ico{position:absolute;width:22px;height:22px;border:2px solid var(--white);border-radius:50%}
</style>
</head>
<body>

<svg class="abs" style="left:0;top:0" width="1200" height="640" aria-hidden="true">
  <polygon points="0,0 1200,0 1200,556 0,612" fill="#1c2463"/>
  <polygon points="0,600 1045,552 1200,540 1200,556 1045,566 0,628" fill="#2f8fe2"/>
</svg>
<div class="abs hero-art" role="img" aria-label="Isometric illustration of a security analyst surrounded by servers and data dashboards"></div>
<header class="abs topbar"></header>
<div class="abs brand">DOMAIN MONITORING</div>
<nav class="abs nav"><a class="active">Home</a><a>Q&amp;A</a><a>Pricing</a><a>About Us</a><a>Contact</a><a>Resources</a></nav>
<h1 class="abs heading hero-title">Prevent attacks<br>by monitoring<br>your domains</h1>
<span class="btn outline-blue" style="left:100px;top:409px;">Learn more</span>

<h2 class="abs heading" style="left:98px;top:718px;">Domain monitoring<br>explainer video</h2>
<div class="abs video" role="img" aria-label="Explainer video thumbnail showing a computer monitor with a light trail"><span class="abs play"></span></div>
<p class="abs copy" style="left:623px;top:722px;width:484px;">Veltrano helps you understand when, where and how stolen or accidentally leaked information is exposed. Veltrano's alerting service can also detect threats before they turn into incidents. There are certain indicators that can be measured. Before an attack takes place, hackers often reserve similar domain names (typosquatting), they spoof profiles in professional networks or they exchange information about targets in hacker forums. Veltrano monitors these activities using "Social Media Monitoring", "Domain Monitoring" and the "Hacker Forum Monitoring". Veltrano's Intelligent Filters and Machine Learning find the real risks among the vast amount of data we collect through human and machine intelligence.</p>
<span class="btn" style="left:623px;top:1114px;">Learn more</span>

<h2 class="abs heading" style="left:100px;top:1500px;">What is the risk?</h2>
<p class="abs copy" style="left:100px;top:1570px;width:450px;font-size:13.5px;line-height:27px;">Hackers use domain-based attacks, which are designed to trick users into submitting sensitive data or downloading dangerous files. This is often the case with phishing attacks. For example, domains can be registered that are very similar to one's own company, a customer or a supplier. Once a fraudulent domain is registered, the hackers try to lure the employee to the website. This can be done via e-mail, SMS (smishing), instant messaging. Social media and many other techniques succeed. A distinction is made between different types of attacks:</p>
<span class="btn" style="left:100px;top:1840px;">Learn more</span>

<div class="risk-card" style="left:605px;top:1455px;height:245px;">
  <svg width="54" height="58" viewBox="0 0 54 58" fill="none" stroke="#1c2463" stroke-width="2"><rect x="8" y="22" width="38" height="30"/><polyline points="8,22 27,38 46,22"/><circle cx="27" cy="14" r="10"/><line x1="27" y1="8" x2="27" y2="15"/><circle cx="27" cy="19" r="1"/></svg>
  <h4>Domain spoofing</h4>
  <p>Here, a domain name is registered that resembles that of a trusted brand or organization.</p>
  <span class="more">READ MORE</span>
</div>
<div class="risk-card" style="left:869px;top:1553px;height:337px;padding-top:80px;">
  <svg width="64" height="60" viewBox="0 0 64 60" fill="none" stroke="#1c2463" stroke-width="2"><rect x="2" y="2" width="60" height="56"/><rect x="6" y="6" width="16" height="6" fill="#2f8fe2" stroke="none"/><polyline points="8,36 18,24 28,40 38,22 48,38 56,30" stroke="#2f8fe2"/><line x1="6" y1="48" x2="58" y2="48"/></svg>
  <h4>Homoglyphic attack</h4>
  <p>This is a variant of domain spoofing. Again, a similar looking domain is registered to.</p>
  <span class="more">READ MORE</span>
</div>
<div class="risk-card" style="left:605px;top:1731px;height:244px;">
  <svg width="64" height="64" viewBox="0 0 64 64" fill="none" stroke="#1c2463" stroke-width="2"><circle cx="32" cy="32" r="29"/><circle cx="32" cy="32" r="22" stroke="#2f8fe2"/><rect x="20" y="26" width="24" height="14" rx="3"/><circle cx="32" cy="33" r="3"/></svg>
  <h4>Typosquatting</h4>
  <p>cybercriminals may attempt to register a malicious domain by using a common company's domain.</p>
  <span class="more">READ MORE</span>
</div>

<svg class="abs" style="left:0;top:2064px" width="1200" height="767" aria-hidden="true">
  <polygon points="0,180 1200,0 1200,767 0,767" fill="#2f8fe2"/>
</svg>
<div class="abs photo-keys" role="img" aria-label="Photo of hands typing on a laptop keyboard with a glowing security lock overlay"></div>
<div class="abs data-box">
  <svg class="abs" style="left:92px;top:40px" width="62" height="62" viewBox="0 0 62 62" fill="none" stroke="#fff" stroke-width="2.5"><circle cx="31" cy="31" r="27"/><circle cx="31" cy="31" r="17"/><circle cx="31" cy="31" r="7"/><line x1="31" y1="31" x2="52" y2="10"/><polyline points="46,8 52,10 54,16"/></svg>
  All data can be<br>analyzed and<br>exported.
</div>
<h2 class="abs heading light" style="left:601px;top:2286px;">How to protect<br>yourself?</h2>
<p class="abs copy light" style="left:607px;top:2415px;width:490px;font-size:13.5px;line-height:29px;">Our domain monitoring solution continuously monitors thousands of TLDs, gTLDs and ccTLDs. For searches, we offer the greatest flexibility in the market and cover ALL forms of attacks. Here are a few examples of search options that can be adopted as active alerts: https://wiki.veltrano.example/docs/domain_database_search</p>
<span class="btn outline" style="left:606px;top:2586px;">Learn more</span>

<h2 class="abs heading" style="left:0;top:2913px;width:1200px;text-align:center;">What else are we monitoring?</h2>
<p class="abs copy" style="left:130px;top:2990px;width:940px;text-align:center;font-size:13.5px;">Veltrano helps you understand when, where and how stolen or accidentally leaked information in dark web markets, forums, botnet logs, IRC, social media and other sources is exposed. Veltrano's alerting service can also detect threats before they turn into incidents. Veltrano offers AI-driven dark web analysis, real-time threat alerts and pre-Attack threat indicators. Setup in minutes you will receive instant access to real-time reporting including:</p>

<div class="mon-card" style="left:98px;top:3174px;">
  <svg width="76" height="70" viewBox="0 0 76 70" fill="none" stroke="#1c2463" stroke-width="2"><path d="M18 30a12 12 0 0 1 4-22a16 16 0 0 1 30 4a10 10 0 0 1 4 18z"/><rect x="26" y="22" width="24" height="8"/><rect x="26" y="32" width="24" height="8"/><line x1="38" y1="40" x2="38" y2="54"/><line x1="14" y1="54" x2="62" y2="54"/><circle cx="14" cy="60" r="5"/><circle cx="38" cy="60" r="5"/><circle cx="62" cy="60" r="5"/></svg>
  <h4>Infrastructure exposure:</h4><p>IoT, code repos, cloud,<br>storage &amp; more</p>
</div>
<div class="mon-card" style="left:358px;top:3219px;">
  <svg width="76" height="70" viewBox="0 0 76 70" fill="none" stroke="#1c2463" stroke-width="2"><circle cx="22" cy="18" r="10"/><circle cx="52" cy="18" r="10"/><circle cx="22" cy="52" r="10"/><circle cx="52" cy="52" r="10"/><rect x="30" y="28" width="16" height="14" stroke="#2f8fe2"/></svg>
  <h4>People exposure:</h4><p>Social media<br>monitoring</p>
</div>
<div class="mon-card" style="left:615px;top:3174px;">
  <svg width="76" height="70" viewBox="0 0 76 70" fill="none" stroke="#1c2463" stroke-width="2"><rect x="8" y="10" width="60" height="42"/><line x1="30" y1="52" x2="26" y2="62"/><line x1="46" y1="52" x2="50" y2="62"/><line x1="20" y1="62" x2="56" y2="62"/><rect x="28" y="28" width="20" height="16" stroke="#2f8fe2"/><path d="M32 28v-6a6 6 0 0 1 12 0v6" stroke="#2f8fe2"/></svg>
  <h4>Ransomware exposure:</h4><p>leak &amp; credential<br>monitoring</p>
</div>
<div class="mon-card" style="left:875px;top:3219px;">
  <svg width="76" height="70" viewBox="0 0 76 70" fill="none" stroke="#1c2463" stroke-width="2"><rect x="8" y="8" width="60" height="44"/><line x1="38" y1="52" x2="38" y2="62"/><line x1="24" y1="62" x2="52" y2="62"/><rect x="24" y="16" width="28" height="28" stroke="#2f8fe2"/><circle cx="38" cy="28" r="6" stroke="#2f8fe2"/></svg>
  <h4>Attack prevention:</h4><p>domain and certificate<br>monitoring</p>
</div>

<svg class="abs" style="left:0;top:3506px" width="1200" height="786" aria-hidden="true">
  <defs><linearGradient id="aboutFill" x1="0" y1="0" x2="1" y2="1"><stop offset="0" stop-color="#2f8fe2"/><stop offset="1" stop-color="#1f6cc4"/></linearGradient></defs>
  <polygon points="0,0 1200,230 1200,786 0,786" fill="url(#aboutFill)"/>
</svg>
<h2 class="abs heading light" style="left:100px;top:3808px;">About us</h2>
<p class="abs copy light" style="left:100px;top:3878px;width:470px;font-size:13.5px;">Veltrano (company registration number CHE-100.200.300) was started in 2018 as a public limited company in Zug, Switzerland. Our analysts have long-standing relationships with various players on the Darknet. These personal relationships make it possible for Veltrano to repeatedly obtain the latest data leaks. Those unique data leaks are published by the press around the world.</p>
<span class="btn outline" style="left:104px;top:4088px;">Learn more</span>
<div class="abs photo-desk" role="img" aria-label="Photo of an analyst working at a desk with several computer screens"></div>

<h2 class="abs heading" style="left:0;top:4394px;width:1200px;text-align:center;">Want to know more?</h2>
<div class="field" style="left:98px;top:4493px;width:321px;">First Name</div>
<div class="field" style="left:440px;top:4493px;width:320px;">Second Name</div>
<div class="field" style="left:779px;top:4493px;width:321px;">Phone Number</div>
<div class="field" style="left:98px;top:4574px;width:1002px;height:111px;">Message</div>
<span class="btn" style="left:535px;top:4724px;width:129px;padding:0;text-align:center;font-size:16px;">Submit</span>

<svg class="abs" style="left:0;top:4870px" width="1200" height="393" aria-hidden="true">
  <polygon points="0,40 1200,0 1200,393 0,393" fill="#1c2463"/>
  <polygon points="0,40 1200,0 1200,8 0,48" fill="#2f8fe2"/>
  <line x1="0" y1="275" x2="1200" y2="275" stroke="#3a4284" stroke-width="1"/>
</svg>
<div class="abs foot-h" style="left:98px;top:4960px;">Domain monitoring</div>
<p class="abs foot-t" style="left:100px;top:5010px;width:330px;">Cyber Threat Intelligence made for swiss banks. Priced for MSSP.</p>
<span class="abs" style="left:100px;top:5090px;width:30px;height:30px;border-radius:50%;background:#fff"></span>
<span class="abs" style="left:146px;top:5090px;width:30px;height:30px;border-radius:50%;background:#fff"></span>

<div class="abs foot-h" style="left:495px;top:4960px;">Call us</div>
<span class="ico" style="left:495px;top:5011px;"></span><p class="abs foot-t" style="left:532px;top:5009px;">+41 790001122</p>
<span class="ico" style="left:495px;top:5052px;"></span><p class="abs foot-t" style="left:532px;top:5050px;">+1 5550143876</p>

<div class="abs foot-h" style="left:717px;top:4960px;">Find us</div>
<span class="ico" style="left:717px;top:5011px;border-radius:50% 50% 50% 0;transform:rotate(-45deg)"></span>
<p class="abs foot-t" style="left:755px;top:5007px;width:160px;line-height:22px;">Veltrano AG, Lindenhofweg 12, 6300 Zug, Switzerland</p>

<div class="abs foot-h" style="left:945px;top:4960px;">Email us</div>
<span class="ico" style="left:945px;top:5011px;"></span><p class="abs foot-t" style="left:984px;top:5007px;">info@veltrano.example</p>

<nav class="abs foot-links"><a>Home</a><a>Q&amp;A</a><a>Pricing</a><a>About Us</a><a>Contact</a><a>Resources</a></nav>
<p class="abs" style="left:0;top:5214px;width:1200px;text-align:center;font-family:'Lato',sans-serif;font-size:11px;color:#fff;">© Veltrano 2022 ALL RIGHTS RESERVED</p>

</body>
</html>
```